Website Design for Law Firm

We need a fresh new website design for our client 'Torvek Legal' who specialises as a Criminal, Traffic & Civil Lawyer in Perth, Western Australia. We are looking for a very clean, professional and elegant look for the website, a presence of power and class needed as he deals with high end clients. Black, Silver and hints of gold need to run through the design without making the site look too dark. We are after a very modern, spacious web look, use of large readable text with links to social media (such as Facebook, Google+, Twitter, LinkedIn) to stand out and his contact details to be made very predominate.

Reason: Public holidays here in Australia, need more business hours to discuss designs with client.

Reason: Client needs more time to look through designs.

Reason: Client is going over last of designs. Design will be picked early next week!

Law Firm

```html
<!DOCTYPE html>
<html lang="en">
<head>
<meta charset="utf-8">
<title>Torvek Legal</title>
<link rel="stylesheet" href="https://fonts.googleapis.com/css2?family=Arimo:wght@400;700&family=Noto+Serif:ital,wght@1,700&family=Oswald:wght@400&display=swap">
<style>
:root{
  --header-grey:#a6a6a6;
  --gold:#d4870d;
  --nav-black:#231f20;
  --band-dark:#4f4f4f;
  --panel-grey:#606060;
  --card-grey:#666666;
  --page-bg:#efefef;
  --white:#ffffff;
  --text:#3a3a3a;
  --footer:#505050;
  --footer-text:#bdbdbd;
}
*{margin:0;padding:0;box-sizing:border-box}
html,body{width:1200px;height:1029px;overflow:hidden}
body{position:relative;background:var(--page-bg);font-family:"Arimo",Arial,sans-serif;color:var(--text)}
.abs{position:absolute}

.site-header{left:0;top:0;width:1200px;height:115px;background:var(--header-grey)}
.header-rule{left:0;top:115px;width:1200px;height:3px;background:var(--gold)}
.brand{left:143px;top:50px;display:flex;align-items:center;gap:8px;font-family:"Arimo",Arial,sans-serif;font-weight:700;font-size:19px;color:var(--nav-black);line-height:1;white-space:nowrap}
.brand-mark{width:14px;height:14px;background:var(--nav-black)}

.main-nav{left:356px;top:39px;width:745px;height:46px;background:var(--nav-black);display:flex;font-family:"Oswald",sans-serif;font-size:15px;color:var(--white)}
.main-nav a{color:inherit;text-decoration:none;display:flex;align-items:center;justify-content:center;height:100%}
.main-nav .active{background:var(--gold)}

.hero-band{left:0;top:118px;width:1200px;height:303px;background:var(--band-dark)}
.slider{left:99px;top:129px;width:659px;height:279px;background:var(--white);padding:8px}
.slide{width:100%;height:100%;background:linear-gradient(90deg,#c9cfd4 0%,#e4e8eb 45%,#d3d8dc 100%)}
.dots{left:384px;top:380px;display:flex;gap:8px}
.dots span{width:9px;height:9px;border-radius:50%;background:var(--white)}
.dots .on{background:var(--gold)}

.contact-panel{left:784px;top:129px;width:317px;height:279px;background:var(--panel-grey);color:var(--white)}
.contact-title{position:absolute;left:29px;top:26px;font-family:"Noto Serif",serif;font-style:italic;font-weight:700;font-size:26px}
.contact-row{position:absolute;left:29px;display:flex;align-items:flex-start;gap:22px;font-family:"Arimo",Arial,sans-serif;font-size:21px;line-height:25px}
.contact-row svg{flex:none}

.content-box{left:99px;top:437px;width:659px;height:511px;background:var(--white);border:1px solid #dcdcdc}
.content-title{position:absolute;left:26px;top:31px;font-family:"Noto Serif",serif;font-style:italic;font-weight:700;font-size:31px;color:var(--gold)}
.content-text{position:absolute;left:32px;top:109px;width:608px;font-size:12.4px;line-height:14.5px}
.content-text p{margin-bottom:14px}

.social{top:439px;width:60px;height:60px;background:var(--band-dark);color:var(--white);text-decoration:none;display:flex;align-items:center;justify-content:center;font-family:"Arimo",Arial,sans-serif;font-weight:700;font-size:13px}

.practice-card{left:784px;width:317px;height:113px;background:var(--card-grey);padding:11px 44px 0 23px;color:var(--white)}
.practice-card h3{font-family:"Noto Serif",serif;font-style:italic;font-weight:700;font-size:16.5px;color:var(--gold);margin-left:-3px;margin-bottom:4px}
.practice-card p{font-size:12.4px;line-height:14.5px}
.practice-card a{display:block;font-size:9.5px;color:var(--gold);text-decoration:none;line-height:13px}

.site-footer{left:99px;top:961px;width:1002px;height:68px;background:var(--footer);color:var(--footer-text);font-family:"Arimo",Arial,sans-serif;font-size:10.5px;text-align:center;padding-top:28px}
</style>
</head>
<body>
<header class="site-header abs"></header>
<div class="header-rule abs"></div>
<div class="brand abs"><span class="brand-mark"></span>TORVEK LEGAL</div>
<nav class="main-nav abs">
  <a class="active" href="#" style="width:99px">HOME</a>
  <a href="#" style="width:162px">ABOUT US</a>
  <a href="#" style="width:146px">SERVICES</a>
  <a href="#" style="width:100px">FAQS</a>
  <a href="#" style="width:85px">BLOG</a>
  <a href="#" style="width:153px">CONTACT US</a>
</nav>

<div class="hero-band abs"></div>
<div class="slider abs">
  <div class="slide" role="img" aria-label="Photo of two lawyers in a consultation across a meeting table"></div>
</div>
<div class="dots abs"><span class="on"></span><span></span><span></span><span></span><span></span></div>

<aside class="contact-panel abs">
  <h2 class="contact-title">Contact us</h2>
  <div class="contact-row" style="top:84px">
    <svg width="28" height="28" viewBox="0 0 28 28"><rect width="28" height="28" rx="5" fill="#fff"/><path d="M9 6c1 0 2 3 2 4s-2 1-1 3 3 4 4 4 1-2 3-1 3 1 3 2-2 3-4 3C10 21 6 14 6 9c0-2 2-3 3-3z" fill="#606060"/></svg>
    <span>444-555-0192</span>
  </div>
  <div class="contact-row" style="top:135px">
    <svg width="31" height="24" viewBox="0 0 31 24" style="margin-top:2px"><rect width="31" height="24" rx="3" fill="#fff"/><path d="M2 3l13.5 11L29 3" stroke="#606060" stroke-width="2.5" fill="none"/></svg>
    <span>info@torveklegal.com</span>
  </div>
  <div class="contact-row" style="top:182px">
    <svg width="26" height="32" viewBox="0 0 26 32"><rect x="1" y="1" width="24" height="30" fill="none" stroke="#fff" stroke-width="2"/><g fill="#fff"><rect x="5" y="5" width="4" height="3"/><rect x="11" y="5" width="4" height="3"/><rect x="17" y="5" width="4" height="3"/><rect x="5" y="11" width="4" height="3"/><rect x="11" y="11" width="4" height="3"/><rect x="17" y="11" width="4" height="3"/><rect x="5" y="17" width="4" height="3"/><rect x="11" y="17" width="4" height="3"/><rect x="17" y="17" width="4" height="3"/><rect x="10" y="23" width="6" height="8"/></g></svg>
    <span>88 Harbour Lane,<br>Eastvale, Australia</span>
  </div>
</aside>

<main class="content-box abs">
  <h1 class="content-title">We are commited to you</h1>
  <div class="content-text">
    <p>Lorem ipsum dolor sit amet, consectetur adipiscing elit. Mauris fermentum interdum vestibulum. Praesent varius scelerisque risus, eu rhoncus lorem. Maecenas convallis nec elit placerat euismod. Ut laoreet tempor tellus, eget fermentum enim consectetur non. Sed vitae auctor mauris, sit amet dictum nulla. Proin viverra porta tellus at porta. Pellentesque suscipit euismod nulla, et eleifend leo gravida eget. Quisque eget aliquet diam, condimentum consectetur massa. Mauris lobortis felis et sagittis luctus. In sed porttitor nisi. Nulla id felis quis neque ultricies consequat. Integer vel eros nisi. Vestibulum nisi eros, tincidunt eu aliquam et, luctus et erat.</p>
    <p>In tempus convallis nisi et mattis. Donec in tincidunt arcu. Nulla facilisi. Praesent pulvinar felis dolor, eget scelerisque neque consectetur vel. Phasellus eget sapien ut libero posuere hendrerit vel in lorem. Nam tristique ipsum lorem, tincidunt tincidunt augue interdum a. Sed faucibus pulvinar nunc quis ultricies. Sed tempus a nunc mollis rutrum. Integer ligula velit, consectetur in nisi eget, varius malesuada dolor. Proin id feugiat enim, rhoncus blandit urna.</p>
    <p>Nunc nec purus molestie, interdum sem ut, aliquet enim. Quisque porta justo id nulla dignissim sollicitudin. Curabitur rhoncus mauris mauris, in commodo risus sagittis nec. In eu turpis elementum justo ultricies molestie. Sed sit amet orci condimentum, adipiscing tortor interdum, mollis sem. Donec et elementum ante. Aliquam eleifend libero non malesuada aliquet.</p>
  </div>
</main>

<a class="social abs" href="#" style="left:784px" aria-label="Social link">Like</a>
<a class="social abs" href="#" style="left:870px" aria-label="Social link">Post</a>
<a class="social abs" href="#" style="left:956px" aria-label="Social link">Share</a>
<a class="social abs" href="#" style="left:1041px" aria-label="Social link">Link</a>

<section class="practice-card abs" style="top:519px">
  <h3>Criminal Law</h3>
  <p>Lorem ipsum dolor sit amet, consectetur adipiscing elit. Mauris fermentum interdum vestibulum.</p>
  <a href="#">READ MORE</a>
</section>
<section class="practice-card abs" style="top:647px">
  <h3>Traffic</h3>
  <p>Lorem ipsum dolor sit amet, consectetur adipiscing elit. Mauris fermentum interdum vestibulum.</p>
  <a href="#">READ MORE</a>
</section>
<section class="practice-card abs" style="top:776px">
  <h3>Civil Law</h3>
  <p>Lorem ipsum dolor sit amet, consectetur adipiscing elit. Mauris fermentum interdum vestibulum.</p>
  <a href="#">READ MORE</a>
</section>

<footer class="site-footer abs">2014 copyright, Torvek Legal</footer>
</body>
</html>
```